NEW Modern Sleek Business Card for VR Language Startup

Our startup is using VR to lead the next wave of world language education. We need a two-sided business card that introduces the larger organization (Quorvel Language Inc) and our contact info on one side and shows the product, Lumidrasca, on the other side.

Side 1 (contact info)= Quorvel Logo and Contact info (name, title, phone, email)

Side 2 (product)= Lumidrasc logo, text, and website
Text= Culturally Immersive Language Learning Games
Website= www.lumidrasc.example

Target Market(s)

Education, Technology

Contact Information for Business Card

Contact info will be updated upon approval of the design. For now, put this as a placeholder.

Perry Hollins
Founder & CEO
phollins@mailtrove.example
(555)-014-2736

Font styles to use
Other font styles liked:
• Gibson and Century Gothic are the brand fonts

Requirements
Nice to have
• I would love to see cohesion between the design and colors of the two logos. I have attached a few business card designs that I like, so you can get a feel for my preferred style.

```html
<!DOCTYPE html>
<html lang="en">
<head>
<meta charset="utf-8">
<title>Quorvel Language – Business Card</title>
<link href="https://fonts.googleapis.com/css2?family=Montserrat:wght@400;500;600&display=swap" rel="stylesheet">
<style>
  :root {
    --backdrop: #1c1c1e;
    --card: #262628;
    --card-edge: #303033;
    --silver: #c9c9cc;
    --muted: #9a9aa0;
    --ink: #f2f2f4;
    --accent: #6f6bd6;
  }
  * { box-sizing: border-box; margin: 0; padding: 0; }
  html, body {
    width: 1200px; height: 900px; overflow: hidden;
    background: var(--backdrop);
    font-family: "Montserrat", "Century Gothic", sans-serif;
    color: var(--ink);
  }
  .sheet {
    position: relative; width: 1200px; height: 900px;
    display: flex; flex-direction: column; align-items: center;
    justify-content: center; gap: 40px;
  }
  .card {
    width: 700px; height: 400px;
    background: var(--card);
    border: 1px solid var(--card-edge);
    position: relative;
  }

  /* Product side */
  .card--product {
    display: flex; flex-direction: column; align-items: center; justify-content: center;
    text-align: center;
  }
  .product-mark {
    display: flex; align-items: center; gap: 18px; margin-bottom: 22px;
  }
  .product-mark__dot {
    width: 26px; height: 26px; border-radius: 50%; background: var(--silver);
  }
  .product-mark__name {
    font-size: 46px; font-weight: 500; letter-spacing: 6px;
    color: var(--silver); text-transform: uppercase;
  }
  .product-tagline {
    font-size: 15px; font-weight: 400; letter-spacing: 3px;
    color: var(--muted); text-transform: uppercase; margin-bottom: 14px;
  }
  .product-site {
    font-size: 16px; font-weight: 400; letter-spacing: 2px; color: var(--silver);
  }

  /* Contact side */
  .card--contact {
    display: flex; align-items: center; padding: 0 60px;
  }
  .contact-brand {
    width: 230px; display: flex; align-items: center; gap: 14px;
  }
  .contact-brand__dot {
    width: 22px; height: 22px; border-radius: 50%; background: var(--accent);
  }
  .contact-brand__name {
    font-size: 32px; font-weight: 500; color: var(--accent); letter-spacing: 2px;
  }
  .divider {
    width: 2px; height: 210px; background: var(--accent); margin: 0 50px 0 20px;
  }
  .contact__name {
    font-size: 34px; font-weight: 600; color: var(--accent);
    letter-spacing: 2px; text-transform: uppercase; line-height: 1.1;
  }
  .contact__title { font-size: 19px; letter-spacing: 1.5px; margin-bottom: 18px; }
  .contact__address { font-size: 18px; letter-spacing: 1.5px; line-height: 1.4; margin-bottom: 12px; }
  .contact__line {
    display: flex; align-items: center; gap: 12px;
    font-size: 18px; letter-spacing: 1.2px; line-height: 1.5;
  }
  .contact__icon { width: 13px; height: 13px; flex: none; }
</style>
</head>
<body>
<main class="sheet">
  <section class="card card--product" aria-label="Card front, product side">
    <div class="product-mark">
      <span class="product-mark__dot"></span>
      <span class="product-mark__name">Lumidrasc</span>
    </div>
    <p class="product-tagline">Culturally Immersive Language Learning Games</p>
    <p class="product-site">www.lumidrasc.example</p>
  </section>

  <section class="card card--contact" aria-label="Card back, contact side">
    <div class="contact-brand">
      <span class="contact-brand__dot"></span>
      <span class="contact-brand__name">Quorvel</span>
    </div>
    <div class="divider"></div>
    <div class="contact">
      <p class="contact__name">Perry Hollins</p>
      <p class="contact__title">Founder &amp; CEO</p>
      <p class="contact__address">48 Marlow Court<br>Brenford, TX 75990</p>
      <p class="contact__line">
        <svg class="contact__icon" viewBox="0 0 16 16" aria-hidden="true"><path d="M3 1h3l1.5 4-2 1.3a9 9 0 0 0 4.2 4.2L11 8.5l4 1.5v3a2 2 0 0 1-2 2A12 12 0 0 1 1 3a2 2 0 0 1 2-2z" fill="#6f6bd6"/></svg>
        555-014-2736
      </p>
      <p class="contact__line">
        <svg class="contact__icon" viewBox="0 0 16 16" aria-hidden="true"><rect x="1" y="3" width="14" height="10" fill="none" stroke="#6f6bd6" stroke-width="1.5"/><path d="M1 3l7 6 7-6" fill="none" stroke="#6f6bd6" stroke-width="1.5"/></svg>
        phollins@mailtrove.example
      </p>
      <p class="contact__line">
        <svg class="contact__icon" viewBox="0 0 16 16" aria-hidden="true"><circle cx="8" cy="8" r="6.5" fill="none" stroke="#6f6bd6" stroke-width="1.5"/><path d="M1.5 8h13M8 1.5c-3 3.5-3 9.5 0 13M8 1.5c3 3.5 3 9.5 0 13" fill="none" stroke="#6f6bd6" stroke-width="1.2"/></svg>
        www.lumidrasc.example
      </p>
    </div>
  </section>
</main>
</body>
</html>
```